Site for company producing and selling products for children's health

We need an appealing professional web site design and images for a brand new company producing and selling products focused on children’s health. The site will offer information to visitors on the company, the company’s products, and general resources related to children’s health. Additionally the site will offer e-commerce functionality to allow for ordering of the company’s products.
The content and navigation for the site will be generated by programming, such as php or asp, and therefore any images used in the navigation portions of the site should allow for HTML markup to be overlaid rather than having the text built into the image or graphic.
The design must include 2 layouts, one for the landing/home page that includes only top navigation, and an inner page layout that includes both top and left navigation.
The header area of the site should include a place for links to access the visitor’s cart and profile similar to the top sections of quillbarn.com, tervodo.com, and pikmart.com.
The landing page of the site should include some type of “changing” image area where we can include multiple image files for rotation to visitors similar to what is seen at vorlo.com or mallowkite.com. The flash/animation mechanism does not need to be provided (although it would be a plus if it was) but the design must accommodate the space for it.
The company’s colors are Orange (FF9900) and Blue (0066FF) and the logo can be viewed at http://corvanelkids.com/logo.png
All CSS and markup provided must be display consistently in Internet Explorer 7+, FifeFox, Google Chrome, and Safari.
Incorporating social media links (facebook, twitter, etc.) is desirable.
Target Market(s)
Parents who are conscious of health risks associated with children's diets and consumer food products.
Industry/Entity Type
E-Commerce
Look and feel
Each slider illustrates characteristics of the customer's brand and the style your logo design should communicate.

```html
<!DOCTYPE html>
<html lang="en">
<head>
<meta charset="utf-8">
<title>corvanelkids – Children's Health</title>
<link href="https://fonts.googleapis.com/css2?family=Arimo:wght@400;700&family=Oswald:wght@300;400&display=swap" rel="stylesheet">
<style>
  :root{
    --page:#ede4d3;
    --orange:#ff9900;
    --orange-dark:#e57f00;
    --orange-light:#ffb52e;
    --blue:#0066ff;
    --blue-deep:#0a3f9e;
    --blue-mid:#1553c9;
    --heading-blue:#0d4fb3;
    --sky:#12c0f2;
    --sky-light:#c9f1fc;
    --panel:#d9d1c0;
    --panel-line:#c4bba8;
    --text:#222;
    --white:#fff;
  }
  *{box-sizing:border-box;margin:0;padding:0}
  html,body{width:1200px;height:1035px;overflow:hidden}
  body{background:var(--page);font-family:"Arimo",Arial,sans-serif;color:var(--text);position:relative}
  .abs{position:absolute}

  /* header */
  .brand{left:152px;top:62px;font:700 28px "Arimo",Arial,sans-serif;color:var(--orange);letter-spacing:-.5px}
  .brand-dot{left:205px;top:18px;width:34px;height:34px;border-radius:50%;background:var(--blue)}
  .account-bar{top:8px;left:815px;display:flex;align-items:center;font-size:12.5px;color:#111}
  .account-bar a{color:#111}
  .login{margin-right:18px}
  .cart-icon{margin-right:6px}
  .account-btn{margin-left:8px;display:inline-block;width:76px;height:19px;border-radius:4px;background:linear-gradient(var(--orange-light),var(--orange-dark));border:1px solid #c56d00;color:#5a2b00;font-size:8.5px;line-height:17px;text-align:center;text-decoration:none}
  .nav{left:325px;top:86px;display:flex}
  .nav a{display:block;width:91px;height:23px;margin-right:1px;background:linear-gradient(#ffb23a,#e78a06);border:1px solid #b86c00;border-bottom:none;border-radius:6px 6px 0 0;color:#222;font-size:12.5px;text-align:center;line-height:22px;text-decoration:none}
  .nav a.active{background:linear-gradient(#ffc23f,#ff9900)}
  .nav a:last-child{width:76px;text-align:left;padding-left:6px}
  .header-bar{left:127px;top:84px}
  .search{left:849px;top:117px;width:170px;height:17px;border:1px solid #9bb;background:var(--white);font:11px Georgia,serif;color:#bbb;padding-left:2px;line-height:15px}
  .go{left:1023px;top:116px;font:700 17px Georgia,serif;color:var(--orange);display:flex;align-items:center;gap:2px}

  /* hero */
  .hero{left:127px;top:171px;width:948px;height:323px;border:1px solid #4a89b8;background:linear-gradient(var(--sky) 0%,#4ccdf5 55%,var(--sky-light) 100%)}
  .hero-frame{left:274px;top:201px;width:665px;height:292px;border:2px solid var(--white);border-bottom:none;border-radius:7px 7px 0 0;background:linear-gradient(100deg,#c9eefc 0%,#3ab9ef 30%,#5ec8f0 50%,#e6c9b8 70%,#c89a84 100%)}
  .hero-title{left:303px;top:300px;font:700 29px/35px "Arimo",Arial,sans-serif;color:var(--white);text-shadow:1px 1px 3px rgba(0,40,90,.45)}

  /* sidebar */
  .categories{left:126px;top:517px;width:213px;height:299px;background:var(--panel);border:1px solid var(--panel-line)}
  .categories h2{position:absolute;left:20px;top:3px;font:300 24px "Oswald",sans-serif;color:#222}
  .categories ul{position:absolute;left:22px;top:47px;list-style:none}
  .categories li{height:21.4px;font-size:13px;color:#333;display:flex;align-items:center}
  .categories li svg{margin-right:9px}
  .newsletter{left:126px;top:828px;width:213px;height:138px;background:linear-gradient(var(--blue) 0%,var(--blue-mid) 60%,var(--blue-deep) 100%);border:1px solid #0b3a8a}
  .newsletter h2{position:absolute;left:11px;top:2px;font:300 23px "Oswald",sans-serif;color:var(--white)}
  .newsletter p{position:absolute;left:12px;top:35px;width:185px;font-size:11.5px;line-height:14px;color:var(--white)}
  .newsletter .field{position:absolute;left:11px;top:70px;width:198px;height:20px;background:var(--white);border:1px solid #888}
  .newsletter .submit{position:absolute;left:121px;top:106px;width:66px;height:28px;border:1px solid #c9dbff;background:linear-gradient(#5aa0ff,#0057d9);color:var(--white);font:700 13px "Arimo",Arial,sans-serif;text-align:center;line-height:26px}

  /* main */
  .welcome{left:351px;top:522px;font:700 23.5px "Arimo",Arial,sans-serif;color:var(--heading-blue)}
  .welcome .hl{color:var(--orange)}
  .intro{left:352px;top:573px;width:516px;font-size:12px;line-height:15.3px;color:#222;text-align:justify}
  .intro p+p{margin-top:31px}
  .read-more{left:808px;top:724px;font:700 11px "Arimo",Arial,sans-serif;color:#111}
  .products-title{left:351px;top:784px;font:700 23.5px "Arimo",Arial,sans-serif;color:var(--heading-blue)}
  .product{top:850px;width:167px;height:116px;background:linear-gradient(#5d8a3a 0%,#9ab06a 45%,#d6b59a 75%,#3c4d6a 100%)}

  /* right tiles */
  .tile{left:876px;width:199px;height:106px;border:1px solid #b56a00;border-radius:6px;background:linear-gradient(160deg,#ffb000 0%,#ff9a00 50%,#e98000 100%);display:flex;align-items:center;justify-content:center;text-align:center;font:700 17.5px/21px "Arimo",Arial,sans-serif;color:#111}

  /* footer */
  .footer{left:126px;top:984px;width:949px;height:49px;background:linear-gradient(var(--blue) 0%,var(--blue-mid) 60%,var(--blue-deep) 100%);border:1px solid #0b3a8a;color:var(--white);font-size:12px;line-height:47px;padding-left:338px}
</style>
</head>
<body>

<header>
  <span class="abs brand-dot"></span>
  <div class="abs brand">corvanelkids</div>

  <div class="abs account-bar">
    <a class="login" href="#">Login</a>
    <svg class="cart-icon" width="26" height="20" viewBox="0 0 26 20" aria-hidden="true">
      <path d="M2 6h22l-3 11H5z" fill="#1fa3e0" stroke="#0c5f9a" stroke-width="1"/>
      <path d="M8 6l4-5M18 6l-4-5" stroke="#0c5f9a" stroke-width="1.5" fill="none"/>
    </svg>
    <a href="#">0 Items</a>&nbsp;($ 0.00)
    <a class="account-btn" href="#">MY ACCOUNT</a>
  </div>

  <svg class="abs header-bar" width="948" height="82" viewBox="0 0 948 82" aria-hidden="true">
    <defs>
      <linearGradient id="barGrad" x1="0" y1="0" x2="0" y2="1">
        <stop offset="0" stop-color="#0a66f0"/>
        <stop offset=".55" stop-color="#1452c4"/>
        <stop offset="1" stop-color="#0b3d96"/>
      </linearGradient>
    </defs>
    <path d="M6 24 H640 C680 24 700 2 730 1 H936 Q947 1 947 12 V74 Q947 81 940 81 H7 Q1 81 1 74 V30 Q1 24 6 24 Z" fill="url(#barGrad)" stroke="#0a2f78"/>
  </svg>

  <nav class="abs nav">
    <a href="#">Home</a>
    <a href="#">About Us</a>
    <a href="#">Products</a>
    <a class="active" href="#">Services</a>
    <a href="#">Contact Us</a>
  </nav>

  <div class="abs search">Search..</div>
  <div class="abs go">GO<svg width="10" height="12" viewBox="0 0 10 12" aria-hidden="true"><path d="M0 0L10 6L0 12Z" fill="#ff9900"/></svg></div>
</header>

<section class="abs hero"></section>
<div class="abs hero-frame" role="img" aria-label="Rotating banner photo of a mother cuddling her smiling baby"></div>
<h1 class="abs hero-title">We Care The Health<br>Of Our Future</h1>

<aside>
  <div class="abs categories">
    <h2>Categories</h2>
    <ul>
      <li><svg width="8" height="10" viewBox="0 0 8 10" aria-hidden="true"><path d="M1 1l5 4-5 4" stroke="#0d4fb3" stroke-width="2" fill="none"/></svg>Categories</li>
      <li><svg width="8" height="10" viewBox="0 0 8 10" aria-hidden="true"><path d="M1 1l5 4-5 4" stroke="#0d4fb3" stroke-width="2" fill="none"/></svg>Categories</li>
      <li><svg width="8" height="10" viewBox="0 0 8 10" aria-hidden="true"><path d="M1 1l5 4-5 4" stroke="#0d4fb3" stroke-width="2" fill="none"/></svg>Categories</li>
      <li><svg width="8" height="10" viewBox="0 0 8 10" aria-hidden="true"><path d="M1 1l5 4-5 4" stroke="#0d4fb3" stroke-width="2" fill="none"/></svg>Categories</li>
      <li><svg width="8" height="10" viewBox="0 0 8 10" aria-hidden="true"><path d="M1 1l5 4-5 4" stroke="#0d4fb3" stroke-width="2" fill="none"/></svg>Categories</li>
      <li><svg width="8" height="10" viewBox="0 0 8 10" aria-hidden="true"><path d="M1 1l5 4-5 4" stroke="#0d4fb3" stroke-width="2" fill="none"/></svg>Categories</li>
      <li><svg width="8" height="10" viewBox="0 0 8 10" aria-hidden="true"><path d="M1 1l5 4-5 4" stroke="#0d4fb3" stroke-width="2" fill="none"/></svg>Categories</li>
      <li><svg width="8" height="10" viewBox="0 0 8 10" aria-hidden="true"><path d="M1 1l5 4-5 4" stroke="#0d4fb3" stroke-width="2" fill="none"/></svg>Categories</li>
      <li><svg width="8" height="10" viewBox="0 0 8 10" aria-hidden="true"><path d="M1 1l5 4-5 4" stroke="#0d4fb3" stroke-width="2" fill="none"/></svg>Categories</li>
      <li><svg width="8" height="10" viewBox="0 0 8 10" aria-hidden="true"><path d="M1 1l5 4-5 4" stroke="#0d4fb3" stroke-width="2" fill="none"/></svg>Categories</li>
      <li><svg width="8" height="10" viewBox="0 0 8 10" aria-hidden="true"><path d="M1 1l5 4-5 4" stroke="#0d4fb3" stroke-width="2" fill="none"/></svg>Categories</li>
    </ul>
  </div>

  <div class="abs newsletter">
    <h2>Newsletter</h2>
    <p>Lorem Ipsum is simply dummy text of the printing and .</p>
    <div class="field"></div>
    <div class="submit">Submit</div>
  </div>
</aside>

<main>
  <h2 class="abs welcome">Welcome to <span class="hl">corvanel</span>kids</h2>
  <div class="abs intro">
    <p>Lorem Ipsum is simply dummy text of the printing and typesetting industry. Lorem Ipsum has been the industry's standard dummy text ever since the 1500s, when an unknown printer took a galley of type and scrambled it to make a type specimen book. It has survived not only five centuries, but also the leap into electronic typesetting,<br>remaining essentially unchanged. It was popularised in the 1960s with the release of Tressmark</p>
    <p>remaining essentially unchanged. It was popularised in the 1960s with the release of Tressmark sheets containing Lorem Ipsum passages, and more recently with desktop publishing software like Quenby Pagework including versions of Lorem Ipsum.</p>
  </div>
  <a class="abs read-more">Read more</a>

  <h2 class="abs products-title">Our Products</h2>
  <div class="abs product" style="left:351px" role="img" aria-label="Product photo of two smiling children outdoors"></div>
  <div class="abs product" style="left:525px" role="img" aria-label="Product photo of two smiling children outdoors"></div>
  <div class="abs product" style="left:699px" role="img" aria-label="Product photo of two smiling children outdoors"></div>
</main>

<div class="abs tile" style="top:517px">CONSUMER<br>PRODUCTS</div>
<div class="abs tile" style="top:631px">FOOD PRODUCTS</div>
<div class="abs tile" style="top:746px">CONSULTING</div>
<div class="abs tile" style="top:860px">TECHNOLOGY</div>

<footer class="abs footer">© 2007-2010 corvanelkids. All Rights Reserved</footer>

</body>
</html>
```